Plimbo brochure design

I would like to design a 11"x 8.5" trifold brochure
This product is a reusable food pouch for kids.
Purpose of this brochure is to educate consumers about it to increase sales.

The general idea of the fold is attached in the powerpoint file this brief. Note that this is just a guide, any creative ideas to better represent the product is welcomed

You can make use of materials and pictures from this link.
https://www.filecrate-example.net/s/x9q2wr7tz4kd8mn/Plimbo%20materials%20for%20design.zip
Updates

Update on brief:
You do not need to follow the colours nor content or placing in my attachment, as is just meant as a guide. 
Feel free to mix it up, be creative. Go wild :)

Target Market(s)

Mother's with babies/kids from 4 months old to 4-years old

Industry/Entity Type

Product

Requirements
Must have
• Clean lines
Simple
Attractive
Nice to have
• Some pictures of fresh fruits/vege especially in the ingredients part.
Think also how to play around with the Fill-Eat-Wash-Repeat process

```html
<!DOCTYPE html>
<html lang="en">
<head>
<meta charset="utf-8">
<title>Plimbo Brochure</title>
<link rel="stylesheet" href="https://fonts.googleapis.com/css2?family=Alfa+Slab+One&family=Arimo:wght@400;700&display=swap">
<style>
  :root {
    --page: #ffffff;
    --ink: #111111;
    --orange: #f55f2e;
    --orange-deep: #e8711a;
    --purple: #9b17f8;
    --lime: #d8f21a;
    --white: #ffffff;
    --frame: #333333;
  }
  * { margin: 0; padding: 0; box-sizing: border-box; }
  html, body { width: 1200px; height: 900px; overflow: hidden; background: var(--page); }
  body { font-family: "Arimo", Arial, sans-serif; color: var(--ink); }
  .canvas { position: relative; width: 1200px; height: 900px; }
  .brochure { position: absolute; left: 53px; top: 30px; width: 1089px; height: 844px; outline: 1px solid var(--frame); }

  .panel { position: absolute; top: 0; height: 844px; }
  .panel--left { left: 0; width: 363px; }
  .panel--middle { left: 363px; width: 363px; background: var(--page); }
  .panel--right { left: 726px; width: 363px; background: var(--purple); }

  .photo { position: absolute; }
  .photo--hero { left: 0; top: 0; width: 363px; height: 486px;
    background: linear-gradient(160deg, #6f8a93 0%, #c9a394 40%, #e9b9a6 60%, #f08a3c 90%); }
  .photo--spoon { left: 0; top: 486px; width: 183px; height: 179px;
    background: linear-gradient(180deg, #bfe6ee 0%, #9fd0dd 60%, #7fb7c8 100%); }
  .photo--snack { left: 183px; top: 486px; width: 180px; height: 179px;
    background: linear-gradient(160deg, #d8e6ea 0%, #ecd5c8 55%, #9fb7c0 100%); }

  .features { position: absolute; left: 0; top: 665px; width: 363px; height: 179px;
    background: var(--orange); list-style: none; padding: 30px 0 0 38px; }
  .features li { color: var(--white); font-size: 14.5px; line-height: 17px; margin-bottom: 9px; }

  .cycle { position: absolute; left: 0; top: 0; }
  .cycle-label { font-family: "Alfa Slab One", Georgia, serif; font-size: 13px; fill: var(--ink); }
  .cycle-title { font-family: "Alfa Slab One", Georgia, serif; font-size: 17px; letter-spacing: 0.5px; fill: var(--ink); }
  .cycle-title .accent { fill: var(--orange-deep); }

  .steps { position: absolute; left: 19px; top: 587px; width: 330px; list-style: none; }
  .steps li { position: relative; padding-left: 26px; font-size: 14.5px; line-height: 17px; margin-bottom: 12px; }
  .steps .num { position: absolute; left: 0; top: -2px; color: var(--orange); font-weight: 700; font-size: 18px; }

  .faq { position: absolute; left: 18px; top: 40px; width: 312px; color: var(--white); }
  .faq h2 { font-family: "Alfa Slab One", Georgia, serif; font-weight: 400; font-size: 11.5px; letter-spacing: 0.6px;
    color: var(--lime); text-transform: uppercase; margin-bottom: 7px; }
  .faq p { font-size: 12px; line-height: 16.5px; margin-bottom: 10px; }
</style>
</head>
<body>
<div class="canvas">
  <div class="brochure">
    <section class="panel panel--left">
      <div class="photo photo--hero" role="img" aria-label="Photo of a toddler sucking food from an orange Plimbo pouch"></div>
      <div class="photo photo--spoon" role="img" aria-label="Photo of a pouch being filled through a funnel stand"></div>
      <div class="photo photo--snack" role="img" aria-label="Photo of a child eating from a printed Plimbo pouch"></div>
      <ul class="features">
        <li>Extra sturdy zip-lock bottom,<br>prevent spills</li>
        <li>Easy-to-clean convenience</li>
        <li>Compatible with spoon attachments</li>
        <li>Easy to fill</li>
      </ul>
    </section>

    <section class="panel panel--middle">
      <svg class="cycle" width="363" height="420" viewBox="0 0 363 420" aria-label="The cycle of Plimbo">
        <defs>
          <g id="arrow">
            <rect x="-11" y="-3" width="14" height="6" fill="#111"/>
            <polygon points="2,-9 12,0 2,9" fill="#111"/>
          </g>
        </defs>
        <rect x="152" y="42" width="35" height="95" rx="17" fill="#f0851e" role="img" aria-label="Carrot icon"/>
        <rect x="281" y="124" width="42" height="80" rx="6" fill="#e8892a" role="img" aria-label="Blender icon"/>
        <rect x="291" y="272" width="34" height="78" rx="10" fill="#f0851e" role="img" aria-label="Filled pouch icon"/>
        <circle cx="184" cy="357" r="35" fill="#fbecc9" role="img" aria-label="Child drinking from a pouch icon"/>
        <rect x="40" y="272" width="34" height="78" rx="10" fill="#9fdaf2" role="img" aria-label="Pouch being washed icon"/>
        <rect x="47" y="128" width="30" height="77" rx="10" fill="#eeeeee" stroke="#111" stroke-width="3" role="img" aria-label="Empty pouch icon"/>

        <text class="cycle-label" x="184" y="158" text-anchor="middle">1</text>
        <text class="cycle-label" x="267" y="201" text-anchor="middle">2</text>
        <text class="cycle-label" x="267" y="282" text-anchor="middle">3</text>
        <text class="cycle-label" x="184" y="319" text-anchor="middle">4</text>
        <text class="cycle-label" x="94" y="282" text-anchor="middle">5</text>
        <text class="cycle-label" x="94" y="201" text-anchor="middle">6</text>

        <use href="#arrow" transform="translate(116,122) rotate(-40)"/>
        <use href="#arrow" transform="translate(243,122) rotate(40)"/>
        <use href="#arrow" transform="translate(305,238) rotate(90)"/>
        <use href="#arrow" transform="translate(252,342) rotate(140)"/>
        <use href="#arrow" transform="translate(117,342) rotate(-140)"/>
        <use href="#arrow" transform="translate(64,238) rotate(-90)"/>

        <text class="cycle-title" x="182" y="232" text-anchor="middle">THE <tspan class="accent">CYCLE</tspan> OF</text>
        <text class="cycle-title" x="182" y="254" text-anchor="middle">PLIMBO</text>
      </svg>

      <ol class="steps">
        <li><span class="num">1.</span>Grab your favorite ingredients.</li>
        <li><span class="num">2.</span>Stick them in the blender (you can skip this step if you are using something that is already squishy, like yougurt or oatmeal).</li>
        <li><span class="num">3.</span>Fill your Plimbo and take it with you.</li>
        <li><span class="num">4.</span>Straight from your bag to your child's hand (and mouth).</li>
        <li><span class="num">5.</span>Pop it in the dishwasher or wash by hand.</li>
        <li><span class="num">6.</span>Plimbo is ready to be filled with fun again.</li>
      </ol>
    </section>

    <section class="panel panel--right">
      <div class="faq">
        <h2>What can I put in a Plimbo?</h2>
        <p>Plimbo refillable pouches are perfect for any squishy food. We fill them with applesauce, smoothies, fruit, grain and veggie purees, homemade baby food, yogurts, oatmeal – anything of a squishy consistency.</p>
        <h2>Where can Plimbo pouches go?</h2>
        <p>Plimbos are easy to fill and take with you wherever you go. School. The park. For homemade baby food, Plimbo reusable squeeze packs mean no more frozen cubes or fussing around with freezer trays, no extra bowls and spoons, and no breakable jars or double-dipping. They can go straight from filling, to the freezer, to your bag, to your child's hand (and mouth) with no fuss (and less mess!).</p>
        <h2>How do I fill my Plimbo?</h2>
        <p>Plimbo pouches can be filled through an extra sturdy zipper located on the bottom of the pouch. Simply turn the pouch over, pull apart the zipper, make sure your cap is on and pour or spoon in your favorite squishy food. For optimal use, Plimbo pouches should be filled about 3⁄4 full depending on the content. Wipe away any seeds or food bits from the zipper, and make sure the bottom is sealed completely after filling. Avoid the microwave, boiling liquids, and anything with a consistency thinner than applesauce.</p>
        <h2>How do I clean my Plimbo?</h2>
        <p>Our pouches were designed specifically for ease of cleaning. Every section of the interior of our pouch is easily rinsed with a direct stream of water. Just pop them in the top rack of your dishwasher or wash them by hand with warm soapy water.</p>
        <h2>About Plimbo &amp; safety materials</h2>
        <p>As eco-minded parents, we made sure Plimbo reusable food pouches are made with the greatest of care. This product is has gone through very stringent test and is US FDA approved. Plimbo are BPA-free, PVC-free, Lead-free, Phthalate-free, puncture resistant plastic, to provide convenience and durability without unnecessary chemicals. ISO 9001 certified and BRC rated, meaning the company meets international standards for quality and safety protocols as pertains to ingredients, allergens, hygiene, humane trade practices, and foreign ingredient exposures.</p>
      </div>
    </section>
  </div>
</div>
</body>
</html>
```